Marketing Brochure design required by Video Production company

We are looking for a slick, professional and eye-catching design for a marketing brochure that will showcase our company and its services.

Purpose:
The purpose of the brochure is to show our company as experienced, capable, professional and creative.

The Brochure:
The brochure will be 10 pages (including front and back cover), designed for printing in measurements of 16cm (height) x 18cm (wide).

Attached you will find:

1. Brochure Copy/Text - this is all the text to be included in the brochure. Text in red colour is not to be included in the design but is there as a guide to assist in the design

2. Design assets - our logo and hi-resolution images to be included in the design. The filenames of the images correspond with pages in the Brochure Copy/Text (as you will see)
* this does not seem to be attaching here in ArtMarketHub. Please download this file from stashbin here: https://www.stashbin.net/s/qk4tr7wnz2lpa0e/Product_Marketing_Brochure_Assets-2016-02-07.zip?dl=0

Design:
We would like the design to be open - not cramped or squashed in. Use of space is good. We want it to look very professional, but creative. And also feel simple and easy to read.

Colours to use - blues with black & white (black & white is our brand).

Please feel free to ask any questions you might have.

Thank you.

Industry/Entity Type

It Company

Font styles to use
Sans Serif

Colors
0592cd
3176b5
3276b5
33a6d7
85cae6
cee9f5
85acd3
eaf1f7

Requirements
Must have
• As per the description.
• Download design assets from:
• https://www.stashbin.net/s/qk4tr7wnz2lpa0e/Product_Marketing_Brochure_Assets-2016-02-07.zip?dl=0

```html
<!DOCTYPE html>
<html lang="en">
<head>
<meta charset="utf-8">
<title>Framewell Media – Brochure Spreads</title>
<link href="https://fonts.googleapis.com/css2?family=Montserrat:wght@300;400;600;700&display=swap" rel="stylesheet">
<style>
:root{
  --blue:#3276b5;
  --blue-light:#85acd3;
  --ink:#231f20;
  --grey:#555;
  --paper:#ffffff;
  --bg:#ececec;
  --font:"Montserrat", Arial, sans-serif;
}
*{box-sizing:border-box;margin:0;padding:0}
html,body{width:1200px;height:1200px;overflow:hidden}
body{background:var(--bg);font-family:var(--font);color:var(--ink)}
.canvas{position:relative;width:1200px;height:1200px}
.spread{position:absolute;background:var(--paper);overflow:hidden;box-shadow:0 2px 10px rgba(0,0,0,.18)}
.spread::after{content:"";position:absolute;top:0;bottom:0;left:50%;width:1px;background:rgba(0,0,0,.08)}
.page{position:absolute;top:0;height:100%}
.photo{position:absolute}

/* logo wordmark */
.wordmark{text-align:center;line-height:1}
.wordmark .name{font-weight:700;letter-spacing:.14em}
.wordmark .sub{font-weight:300;letter-spacing:.6em;display:block;margin-top:4px}

/* cover spread */
.cover{left:150px;top:40px;width:900px;height:400px}
.cover .page{width:450px}
.back{left:0}
.front{left:450px}
.back .wordmark{position:absolute;top:48px;left:0;width:100%}
.back .wordmark .name{font-size:28px}
.back .wordmark .sub{font-size:9px;color:var(--grey)}
.get-in-touch{position:absolute;top:135px;width:100%;text-align:center;font-weight:300;font-size:19px}
.contact{position:absolute;top:320px;left:0;width:100%;text-align:center;font-weight:300;font-size:13px;line-height:1.55;list-style:none}
.contact li{display:flex;align-items:center;justify-content:center;gap:6px}
.contact svg{width:12px;height:12px}
.front .strip{position:absolute;left:240px;top:0;width:210px;height:100%;background:var(--ink)}
.front .band{position:absolute;left:232px;top:175px;width:218px;height:120px;background:var(--blue);display:flex;align-items:center;justify-content:center}
.front .band .name{font-size:20px;color:#fff}
.front .band .sub{font-size:7px;color:var(--blue-light)}
.tagline{position:absolute;left:52px;top:318px;font-weight:300;font-size:20px;line-height:1.2}

/* inner spreads */
.inner{width:560px;height:249px}
.s1{left:30px;top:485px}.s2{left:610px;top:485px}
.s3{left:30px;top:775px}.s4{left:610px;top:775px}
.inner .page{width:280px}
.inner .left{left:0}.inner .right{left:280px}
.band{position:absolute;left:0;width:100%;top:108px;height:78px;background:var(--blue)}
.body-text{position:absolute;font-size:5.2px;line-height:1.5;color:var(--grey);font-weight:400}
.body-text p+p{margin-top:4px}
.body-text b{color:var(--ink);font-weight:600}
.band-title{position:absolute;top:136px;font-size:13px;line-height:1.15;color:#fff;font-weight:300}
.band-title strong{font-weight:600;color:var(--ink)}
.includes{position:absolute;top:194px;font-size:5px;line-height:1.45;color:var(--grey)}
.includes h4{font-size:5.4px;font-weight:600;color:var(--ink);margin-bottom:2px}
.tick-list{list-style:none}
.tick-list li{display:flex;align-items:flex-start;gap:3px}
.tick-list svg{width:5px;height:5px;flex:none;margin-top:1px}
.bar{position:absolute;left:10px;top:226px;width:260px;height:15px;background:var(--ink);color:#fff;font-size:4.8px;display:flex;align-items:center;justify-content:center;font-weight:300}
.bar .num{position:absolute;font-size:5px;font-weight:600;width:7px;height:7px;background:#fff;color:var(--ink);display:flex;align-items:center;justify-content:center;top:4px}
.left .bar .num{left:5px}.right .bar .num{right:5px}
.mini-logo{position:absolute;top:14px;right:14px}
.mini-logo .name{font-size:7.5px}
.mini-logo .sub{font-size:2.6px;color:var(--grey);margin-top:2px}

.bespoke{position:absolute;left:12px;top:121px;width:248px;height:54px;border:1px solid #fff;color:#fff;text-align:center;font-size:5px;line-height:1.7;font-weight:300;padding-top:6px}
.bespoke h3{font-size:5.6px;font-weight:600;margin-bottom:2px}
.partners-intro{position:absolute;left:12px;top:200px;width:100px;font-size:5.6px;font-style:normal;font-weight:300;color:var(--grey);line-height:1.4}
.partners{position:absolute;left:140px;top:198px;font-size:5px;line-height:1.65;font-weight:600}
.page-no{position:absolute;right:12px;bottom:12px;font-size:5px;font-weight:700;background:var(--ink);color:#fff;width:7px;height:7px;display:flex;align-items:center;justify-content:center}

.service-h{position:absolute;font-size:12px;font-weight:300;line-height:1}
.service-h strong{font-weight:600}
</style>
</head>
<body>
<svg width="0" height="0" style="position:absolute" aria-hidden="true">
  <symbol id="tick" viewBox="0 0 10 10"><circle cx="5" cy="5" r="4.2" fill="none" stroke="#3276b5" stroke-width="1.2"/><path d="M3 5.2l1.5 1.5L7.2 3.6" fill="none" stroke="#3276b5" stroke-width="1.3"/></symbol>
</svg>

<main class="canvas">

  <!-- Cover spread: back cover + front cover -->
  <section class="spread cover">
    <div class="page back">
      <div class="wordmark"><span class="name">FRAMEWELL</span><span class="sub">MEDIA</span></div>
      <h2 class="get-in-touch">GET IN TOUCH:</h2>
      <div class="photo" role="img" aria-label="Guests dancing at a lively evening event under warm stage lights" style="left:30px;top:178px;width:390px;height:125px;background:linear-gradient(100deg,#2a0e0e 0%,#5a1c1c 35%,#3a2440 60%,#1a0c0c 100%)"></div>
      <ul class="contact">
        <li><svg viewBox="0 0 12 12"><circle cx="6" cy="6" r="6" fill="#3276b5"/><rect x="3.5" y="3" width="5" height="6" fill="#fff"/></svg>PO Box 4120 Elmridge VIC 3199</li>
        <li><svg viewBox="0 0 12 12"><circle cx="6" cy="6" r="6" fill="#3276b5"/><path d="M4 3.2c.6 2.6 2 4.2 4.8 5.4l.4-1.2-1.5-.7-.6.6C6 6.7 5.3 6 5 5.1l.6-.6-.6-1.5z" fill="#fff"/></svg>+61 3 5550 0142</li>
        <li><svg viewBox="0 0 12 12"><circle cx="6" cy="6" r="6" fill="#3276b5"/><rect x="3" y="4" width="6" height="4" fill="none" stroke="#fff" stroke-width=".8"/><path d="M3 4l3 2.2L9 4" fill="none" stroke="#fff" stroke-width=".8"/></svg>info@framewellmedia.com.au</li>
        <li><svg viewBox="0 0 12 12"><circle cx="6" cy="6" r="6" fill="#3276b5"/><circle cx="6" cy="6" r="3.2" fill="none" stroke="#fff" stroke-width=".7"/><path d="M2.8 6h6.4M6 2.8v6.4" stroke="#fff" stroke-width=".6"/></svg>www.framewellmedia.com.au</li>
      </ul>
    </div>
    <div class="page front">
      <div class="strip"></div>
      <div class="photo" role="img" aria-label="Row of ceramic vases against a warm orange wall" style="left:30px;top:175px;width:202px;height:120px;background:linear-gradient(90deg,#c8581c 0%,#e07a2a 45%,#f0a040 100%)"></div>
      <div class="band"><div class="wordmark"><span class="name">FRAMEWELL</span><span class="sub">MEDIA</span></div></div>
      <h1 class="tagline">CREATIVE<br>VIDEO<br>CONTENT</h1>
    </div>
  </section>

  <!-- Spread pages 2–3: introduction -->
  <section class="spread inner s1">
    <div class="band"></div>
    <div class="page left">
      <div class="body-text" style="left:12px;top:24px;width:250px">
        <p><b>FRAMEWELL MEDIA</b> produces creative video content for brands and organisations that seek to build, engage and grow their audiences. Whether your business is getting its feet wet in the videosphere or looking to take your creative communications to the next level, we can deliver. We identify your story and what makes you unique, then marry this with super creative and killer production values via a team of filmmakers, creative strategists, writers, designers and animators.</p>
      </div>
      <div class="bespoke">
        <h3>BESPOKE VIDEO SOLUTIONS</h3>
        IF YOU'VE GOT A SPECIFIC IDEA OR BRIEF IN MIND, GREAT!<br>
        LET US HELP DEVELOP IT AND MAKE IT REALITY.<br>
        OTHERWISE, READ ON TO FIND OUT MORE ABOUT OUR OFFERING.
      </div>
      <div class="body-text" style="left:12px;top:196px;width:250px">
        <p>We work with organisations that want to cultivate a digital relationship across all channels and screens through creative video marketing. Our portfolio includes ads for web &amp; TV, corporate profiles, recruitment &amp; training videos, documentary-style shorts and music videos.</p>
        <p>We understand that how you present your brand visually requires tact and thought. Talk to us today about how we can help grow your business.</p>
      </div>
    </div>
    <div class="page right">
      <div class="mini-logo wordmark"><span class="name">FRAMEWELL</span><span class="sub">MEDIA</span></div>
      <div class="photo" role="img" aria-label="Close-up portrait of a person sipping coffee in warm tones" style="left:0;top:50px;width:140px;height:118px;background:linear-gradient(135deg,#3b2a22,#8a6a52 60%,#c9b39a)"></div>
      <div class="photo" role="img" aria-label="Portrait of a man against a pale wall" style="left:142px;top:50px;width:126px;height:118px;background:linear-gradient(135deg,#e8e4de,#b89a80 60%,#7a5a44)"></div>
      <p class="partners-intro">Some of the organisations we've partnered with include:</p>
      <ul class="tick-list partners">
        <li><svg><use href="#tick"/></svg>Carrow University</li>
        <li><svg><use href="#tick"/></svg>Eastside Hawkers FC</li>
        <li><svg><use href="#tick"/></svg>State Office of Riverland</li>
        <li><svg><use href="#tick"/></svg>Lantern News Group</li>
        <li><svg><use href="#tick"/></svg>City of Marlowe</li>
        <li><svg><use href="#tick"/></svg>Regional Electoral Office</li>
        <li><svg><use href="#tick"/></svg>Brookvale Racing Club</li>
      </ul>
      <span class="page-no">3</span>
    </div>
  </section>

  <!-- Spread pages 4–5: story and event -->
  <section class="spread inner s2">
    <div class="band"></div>
    <div class="page left">
      <div class="body-text" style="left:12px;top:22px;width:250px">
        <p>The Your STORY video profile is a combination of interviews and overlay footage designed to tell your business' story.</p>
        <p><b>This style of video content helps your audience better understand:</b></p>
        <ul class="tick-list">
          <li><svg><use href="#tick"/></svg>what makes you unique</li>
          <li><svg><use href="#tick"/></svg>why they should trust you</li>
          <li><svg><use href="#tick"/></svg>what your product offering is and how it works</li>
          <li><svg><use href="#tick"/></svg>what your process is</li>
        </ul>
        <p>We'll work with you to develop the best approach to deliver this in a sharp &amp; engaging fashion.</p>
      </div>
      <h3 class="band-title" style="left:14px">YOUR <strong>STORY</strong><br><strong>VIDEO</strong> PROFILE</h3>
      <div class="photo" role="img" aria-label="Editor working at a desk with studio monitors" style="left:135px;top:108px;width:140px;height:78px;background:linear-gradient(120deg,#2a2622,#5a4a3c 55%,#8a7a68)"></div>
      <div class="includes" style="left:12px;width:255px">
        <h4>The package includes:</h4>
        <ul class="tick-list">
          <li><svg><use href="#tick"/></svg>Filming of interviews + overlay footage at your desired location</li>
          <li><svg><use href="#tick"/></svg>A slick, professionally edited high definition video</li>
          <li><svg><use href="#tick"/></svg>Quick turnaround time and review process</li>
          <li><svg><use href="#tick"/></svg>An opportunity to make any changes before your video is finalised</li>
          <li><svg><use href="#tick"/></svg>Delivery in your choice of formats</li>
        </ul>
      </div>
      <div class="bar"><span class="num">4</span>Have additional requirements? No problem. Contact us to discuss a quote</div>
    </div>
    <div class="page right">
      <div class="body-text" style="left:12px;top:18px;width:120px">
        <p>Got a launch, seminar, celebration, party or any other event that you want filmed? We've got you covered.</p>
        <p>The Your EVENT package provides creative event coverage, with the best parts of your event condensed into a slick highlights video that captures the vibe and essence of your event.</p>
      </div>
      <div class="photo" role="img" aria-label="Speakers on stage under a spotlight at a conference" style="left:150px;top:28px;width:120px;height:92px;background:linear-gradient(160deg,#0e1a3a,#24345e 55%,#0a0a14)"></div>
      <h3 class="band-title" style="left:12px">YOUR <strong>EVENT</strong><br><strong>EVENT</strong> COVERAGE &amp; HIGHLIGHTS</h3>
      <div class="includes" style="left:12px;width:255px">
        <h4>The package includes:</h4>
        <ul class="tick-list">
          <li><svg><use href="#tick"/></svg>Filming of your event exactly as you need</li>
          <li><svg><use href="#tick"/></svg>A slick, professionally edited high definition video, cut to music to suit your event</li>
          <li><svg><use href="#tick"/></svg>An opportunity to review an edit and make changes before your video is finalised</li>
          <li><svg><use href="#tick"/></svg>Delivery in your choice of formats</li>
          <li><svg><use href="#tick"/></svg>Speech &amp; speaker recording also available</li>
        </ul>
      </div>
      <div class="bar"><span class="num">5</span>Have additional requirements? No problem. Contact us to discuss a quote</div>
    </div>
  </section>

  <!-- Spread pages 6–7: explainer and client -->
  <section class="spread inner s3">
    <div class="band"></div>
    <div class="page left">
      <div class="body-text" style="left:12px;top:22px;width:110px">
        <p>If you're looking to convey your message in a simple, easy-to-understand fashion, then consider an EXPLAINER Animation (or infographic). Suitable for businesses with more complex offerings, and where trust is vital, an explainer animation is a highly informative video that brings to life a script via clever animation and voiceover. Think fun and eye-catching.</p>
      </div>
      <div class="photo" role="img" aria-label="Flat illustration of a modern building with trees" style="left:125px;top:36px;width:145px;height:86px;background:linear-gradient(135deg,#eaf1f7,#cee9f5 50%,#85acd3)"></div>
      <h3 class="band-title" style="left:12px">EXPLAINER <strong>ANIMATION</strong><br><strong>ANIMATED</strong> EXPLAINER</h3>
      <div class="includes" style="left:12px;width:255px">
        <h4>The package includes:</h4>
        <ul class="tick-list">
          <li><svg><use href="#tick"/></svg>Script development based on your key messages and target market</li>
          <li><svg><use href="#tick"/></svg>Planning, storyboarding and design consistent with your brand</li>
          <li><svg><use href="#tick"/></svg>Professional voiceover recording, with your preferred style of voice</li>
          <li><svg><use href="#tick"/></svg>A slick, professionally edited high definition animated video, cut to appropriate music</li>
          <li><svg><use href="#tick"/></svg>Titles and a call to action to drive home your message</li>
        </ul>
      </div>
      <div class="bar"><span class="num">6</span>Have additional requirements? No problem. Contact us to discuss a quote</div>
    </div>
    <div class="page right">
      <div class="body-text" style="left:12px;top:18px;width:255px">
        <p>Leverage your customer relationships and use their success stories to build trust and acquire new business. The Your CLIENT package is a testimonial video that gets your current clientele speaking</p>
      </div>
      <div class="body-text" style="left:12px;top:38px;width:115px">
        <p>to your prospective clientele, telling them all the reasons why they should do business with you. Sometimes it's better coming from someone else. We'll work with you to develop a key message and talking points that show you in the best light possible.</p>
      </div>
      <div class="photo" role="img" aria-label="Business owner speaking in a bright studio office" style="left:140px;top:40px;width:130px;height:80px;background:linear-gradient(135deg,#d8d2c8,#a89684 55%,#4a4038)"></div>
      <h3 class="band-title" style="left:12px">YOUR <strong>CLIENT</strong><br><strong>CUSTOMER</strong> TESTIMONIAL VIDEO</h3>
      <div class="includes" style="left:12px;width:255px">
        <h4>The package includes:</h4>
        <ul class="tick-list">
          <li><svg><use href="#tick"/></svg>Filming &amp; interviewing of your client at a location of choice</li>
          <li><svg><use href="#tick"/></svg>A slick, professionally edited high definition video</li>
          <li><svg><use href="#tick"/></svg>An opportunity to review an edit and make changes before your video is finalised</li>
          <li><svg><use href="#tick"/></svg>Delivery in your choice of formats</li>
        </ul>
      </div>
      <div class="bar"><span class="num">7</span>Have additional requirements? No problem. Contact us to discuss a quote</div>
    </div>
  </section>

  <!-- Spread pages 8–9: social content and production services -->
  <section class="spread inner s4">
    <div class="band"></div>
    <div class="page left">
      <div class="photo" role="img" aria-label="Young man working in a dim warm-lit room" style="left:0;top:0;width:280px;height:108px;background:linear-gradient(110deg,#1a0c08,#5a2a1a 45%,#a86a4a 75%,#3a1e14)"></div>
      <h3 class="band-title" style="left:12px">SOCIAL <strong>CONTENT</strong><br><strong>SHORT</strong> FORM SOCIAL MEDIA CONTENT</h3>
      <div class="body-text" style="left:12px;top:196px;width:255px">
        <p>Increase the effectiveness of your video campaign by producing short form versions designed specifically for social media. This allows your videos to be seen across more platforms, engaging your social communities and extending the life of your content. We can turn anything we produce into content relevant for PicStream, FriendLoop, WorkLink and other platforms.</p>
      </div>
      <div class="bar"><span class="num">8</span>Have additional requirements? No problem. Contact us to discuss a quote</div>
    </div>
    <div class="page right">
      <div class="mini-logo wordmark"><span class="name">FRAMEWELL</span><span class="sub">MEDIA</span></div>
      <h3 class="service-h" style="left:12px;top:56px"><strong>FILMING</strong> ONLY</h3>
      <div class="body-text" style="left:12px;top:74px;width:255px"><p>Got your own editing suite and just need the footage? We can film whatever you need and then hand the footage over upon completion. Half Day or Full Day rates available.</p></div>
      <h3 class="service-h" style="left:12px;top:122px;color:#fff"><strong style="color:var(--ink)">EDITING</strong> ONLY</h3>
      <div class="body-text" style="left:12px;top:140px;width:255px;color:#eaf1f7"><p>Got footage that requires some slicing, dicing and polish? We can edit your own footage and give it that sparkle it needs in terms of visuals and audio.</p></div>
      <h3 class="service-h" style="left:12px;top:194px"><strong>AUDIO</strong> CLEAN UP</h3>
      <div class="body-text" style="left:12px;top:208px;width:255px;font-size:4.6px;line-height:1.35"><p>If you're filming content in-house, poor audio can spoil it. We can help with the clean up of audio, including reducing hiss, hum and crackle.</p></div>
      <div class="bar" style="top:229px;height:13px"><span class="num" style="top:3px">9</span>Have additional requirements? No problem. Contact us to discuss a quote</div>
    </div>
  </section>

</main>
</body>
</html>
```